Home Refinance . Residential Mortgages

I want to post a small flyer as part of an email. I want do an email blast. I am a mortgage company and want to entice borrowers with my low interest rates. My website is www.brookmerelending.com
The colors must match the website colors.
QT BRSL REFINANCE.
30 YR. FIXED RATES as low as
2.25% | 2.437% APR
No Appraisal, No out of Pocket cost, NO Income Verification, NO Asset Verification, Close in 30 days or less

Target Market(s)

Real Estate agents & Borrowers looking to get a mortgage loan

Colors
0455a3
ec1f27
28a1d5

Requirements
Must have
• The colors must match the website colors.
BROOKMERE LENDING, INC,.
4817B Halloway Road
Alexandria, VA 58147
RLCB 5830276
www.rlcbborrowerlookup.com

Open Keystone Allegiance LOGO.

```html
<!DOCTYPE html>
<html lang="en">
<head>
<meta charset="utf-8">
<title>QT BRSL Refinance – Brookmere Lending</title>
<link href="https://fonts.googleapis.com/css2?family=Quicksand:wght@400;500;600;700&display=swap" rel="stylesheet">
<style>
  :root {
    --navy-deep: #0a2563;
    --navy: #0c2a6a;
    --brand-blue: #0455a3;
    --sky: #28a1d5;
    --white: #ffffff;
    --ink: #2a2a2a;
    --photo-tone-a: #c9ccd3;
    --photo-tone-b: #5a5e6a;
    --photo-tone-c: #a48468;
  }
  * { margin: 0; padding: 0; box-sizing: border-box; }
  html, body { width: 1200px; height: 795px; overflow: hidden; background: var(--white); }
  .flyer {
    position: relative;
    width: 1200px;
    height: 795px;
    overflow: hidden;
    background: var(--white);
    font-family: "Quicksand", sans-serif;
  }
  .flyer-art { position: absolute; inset: 0; width: 1200px; height: 795px; }
  .site-url {
    position: absolute;
    top: 40px;
    left: 700px;
    width: 480px;
    text-align: center;
    font-size: 23px;
    font-weight: 500;
    letter-spacing: 4.2px;
    color: var(--ink);
  }
  .offer { position: absolute; left: 0; top: 0; color: var(--white); }
  .program {
    position: absolute;
    left: 95px; top: 124px;
    white-space: nowrap;
    font-size: 33px;
    font-weight: 400;
    letter-spacing: 4.5px;
  }
  .headline {
    position: absolute;
    left: 91px; top: 228px;
    white-space: nowrap;
    font-size: 67px;
    font-weight: 700;
    letter-spacing: 3px;
  }
  .lead-in {
    position: absolute;
    left: 89px; top: 344px;
    white-space: nowrap;
    font-size: 35px;
    font-weight: 400;
    letter-spacing: 5px;
  }
  .rates {
    position: absolute;
    left: 86px; top: 432px;
    display: flex;
    align-items: center;
    white-space: nowrap;
    font-size: 42px;
    font-weight: 500;
    letter-spacing: 2px;
  }
  .rates-divider {
    display: block;
    width: 2px;
    height: 58px;
    background: var(--white);
    margin: 0 36px 0 37px;
  }
  .benefits {
    position: absolute;
    left: 89px; top: 588px;
    list-style: none;
    font-size: 16px;
    font-weight: 400;
    letter-spacing: 2.3px;
    line-height: 32.5px;
    white-space: nowrap;
  }
  .benefits .benefit-strong { font-weight: 600; letter-spacing: 1.2px; }
  .cta {
    position: absolute;
    left: 759px; top: 708px;
    width: 315px; height: 70px;
    border-radius: 35px;
    background: linear-gradient(90deg, var(--brand-blue) 0%, #1b7fc4 55%, #21b0e6 100%);
    color: var(--white);
    display: flex;
    align-items: center;
    justify-content: center;
    gap: 20px;
    text-decoration: none;
    padding-left: 18px;
  }
  .cta-label { font-size: 26px; font-weight: 600; letter-spacing: 3.6px; }
  .cta-icon { width: 28px; height: 30px; }
</style>
</head>
<body>
<main class="flyer">
  <svg class="flyer-art" viewBox="0 0 1200 795" aria-hidden="false">
    <defs>
      <linearGradient id="panelGradient" x1="0" y1="0" x2="0.35" y2="1">
        <stop offset="0" stop-color="#0d2b6e"/>
        <stop offset="0.3" stop-color="#0a2563"/>
        <stop offset="0.6" stop-color="#0d4a8c"/>
        <stop offset="1" stop-color="#1c8fc8"/>
      </linearGradient>
      <linearGradient id="photoGradient" x1="0" y1="0" x2="1" y2="1">
        <stop offset="0" stop-color="#5a5e6a"/>
        <stop offset="0.45" stop-color="#9a9ea8"/>
        <stop offset="0.75" stop-color="#c9ccd3"/>
        <stop offset="1" stop-color="#a48468"/>
      </linearGradient>
    </defs>
    <polygon class="photo-area" role="img"
      aria-label="Photo: a loan officer in a suit hands over house keys across a desk with a model house, paperwork and a calculator"
      points="640,104 1200,104 1200,690 597,690" fill="url(#photoGradient)"/>
    <polygon class="offer-panel" points="0,0 663,0 592,795 0,795" fill="url(#panelGradient)"/>
  </svg>

  <p class="site-url">www.brookmerelending.com</p>

  <section class="offer">
    <p class="program">QT BRSL REFINANCE</p>
    <h1 class="headline">FIXED RATES</h1>
    <p class="lead-in">as low as</p>
    <p class="rates">
      <span class="rate">2.25%</span>
      <span class="rates-divider"></span>
      <span class="apr">2.437% APR</span>
    </p>
    <ul class="benefits">
      <li>NO APPRAISAL, NO OUT OF POCKET COST,</li>
      <li>NO INCOME VERIFICATION, NO ASSET VERIFICATION,</li>
      <li class="benefit-strong">CLOSE IN 30 DAYS OR LESS</li>
    </ul>
  </section>

  <a class="cta" href="#">
    <span class="cta-label">GET STARTED</span>
    <svg class="cta-icon" viewBox="0 0 28 30" aria-hidden="true">
      <polyline points="3,2 14,15 3,28" fill="none" stroke="#ffffff" stroke-width="3" stroke-linejoin="round" stroke-linecap="round"/>
      <polyline points="13,2 24,15 13,28" fill="none" stroke="#ffffff" stroke-width="3" stroke-linejoin="round" stroke-linecap="round"/>
    </svg>
  </a>
</main>
</body>
</html>
```